Personal Injury Law Firm in Alaska Needs a Banner Ad Design

Pellmar Law Group is a law firm based in Anchorage, Alaska that specializes in personal injury cases. We are an experienced, professional, and successful legal team that takes pride in always putting the needs of our clients first. Our mission is to secure fair compensation for our clients when they've been injured in an accident or otherwise due to another party's negligence.
We need a banner ad that draws potential clients to our website, where they can call us or submit a description of their case for a free initial consultation. We would like to see designs that are sharp, professional, and sophisticated. The ad should communicate some of our firm's defining qualities: knowledge, experience, compassion, and a strong work ethic.
We need a design that will work for image ads that are vertically oriented (160x600 or similar), horizontally oriented (600x160 or similar), and almost-square (300x250 or similar). Alternatively, we need three different designs that work for each orientation. The general proportions of your designs are more important than specific sizes.
We have included a dropbox file of photos to use as inspiration or incorporate into your design.
Target Market(s)
Victims of vehicular accidents, workplace injury, medical malpractice, etc.
Industry/Entity Type
Law Firm
Look and feel

```html
<!DOCTYPE html>
<html lang="en">
<head>
<meta charset="utf-8">
<title>Pellmar Law Group — Banner Ad Set</title>
<link rel="stylesheet" href="https://fonts.googleapis.com/css2?family=Lato:wght@400;700&display=swap">
<style>
:root{
  --stage:#262626;
  --label:#d4d4d4;
  --blue-light:#6791b2;
  --blue-mid:#5a84a5;
  --blue-deep:#4c7596;
  --white:#ffffff;
  --ink:#1f3a5c;
  --button-bg:#e4e8ec;
  --photo-warm:#6b3d25;
  --photo-cool:#5f7f93;
  --photo-dark:#2b2a2d;
}
*{margin:0;padding:0;box-sizing:border-box}
html,body{width:1200px;height:1195px;overflow:hidden;background:var(--stage)}
body{font-family:"Lato",Arial,sans-serif}
.artboard{position:relative;width:1039px;height:1035px;transform:scale(1.155);transform-origin:0 0}
.banner{position:absolute;overflow:hidden;background:linear-gradient(160deg,var(--blue-light),var(--blue-mid) 55%,var(--blue-deep))}
.photo{position:absolute;background:linear-gradient(90deg,var(--photo-warm) 0%,var(--photo-dark) 30%,var(--photo-cool) 55%,var(--blue-mid) 100%)}
.photo--fade{background:linear-gradient(90deg,var(--photo-warm) 0%,var(--photo-dark) 20%,var(--photo-cool) 45%,var(--blue-mid) 62%,var(--blue-mid) 100%)}
.brand{position:absolute;background:var(--white);display:flex;align-items:center;gap:4px;padding:0 5px;color:var(--ink);font-weight:700;white-space:nowrap;line-height:1}
.brand__mark{width:12%;aspect-ratio:1;background:var(--ink);flex:none}
.headline{position:absolute;right:0;color:var(--white);font-weight:700;text-align:right;line-height:1}
.sub{position:absolute;color:var(--white);font-weight:700;text-align:right;line-height:1.3}
.cta{position:absolute;background:var(--button-bg);color:var(--ink);display:flex;align-items:center;justify-content:space-between;padding:0 3px 0 6px;white-space:nowrap}
.cta svg{flex:none}
.size-label{position:absolute;color:var(--label);font-size:13px}
</style>
</head>
<body>
<div class="artboard">

  <!-- 160x600 -->
  <div class="banner" style="left:79px;top:81px;width:160px;height:600px">
    <div class="brand" style="left:69px;top:28px;width:82px;height:28px;font-size:8px"><span class="brand__mark"></span>Pellmar Law Group</div>
    <h2 class="headline" style="top:75px;right:8px;font-size:28px;line-height:28px">Alaska<br>Personal<br>Injury<br>Attorneys</h2>
    <p class="sub" style="top:195px;right:8px;font-size:13px;line-height:17px">Learn more before you<br>talk to the adjuster</p>
    <div class="cta" style="left:63px;top:240px;width:91px;height:22px;font-size:12px">Learn More<svg width="14" height="14" viewBox="0 0 14 14"><circle cx="7" cy="7" r="7" fill="#1f3a5c"/><path d="M5.5 4v6l4.5-3z" fill="#fff"/></svg></div>
    <div class="photo" role="img" aria-label="Photo of an attorney in conversation with a client in an office" style="left:0;top:293px;width:160px;height:307px"></div>
  </div>
  <span class="size-label" style="left:183px;top:686px">160x600</span>

  <!-- 300x600 -->
  <div class="banner" style="left:287px;top:81px;width:300px;height:600px">
    <div class="brand" style="left:170px;top:22px;width:113px;height:38px;font-size:10px"><span class="brand__mark"></span>Pellmar Law Group</div>
    <h2 class="headline" style="top:83px;right:13px;font-size:36px;line-height:37px">Compassionate,<br>knowledgeable,<br>experienced</h2>
    <p class="sub" style="top:210px;right:13px;font-size:14px;line-height:17px">We've been helping accident<br>victims like you since 1993</p>
    <div class="cta" style="left:144px;top:256px;width:145px;height:22px;font-size:12px">For a free consultation<svg width="14" height="14" viewBox="0 0 14 14"><circle cx="7" cy="7" r="7" fill="#1f3a5c"/><path d="M5.5 4v6l4.5-3z" fill="#fff"/></svg></div>
    <div class="photo" role="img" aria-label="Photo of an attorney in conversation with a client in an office" style="left:0;top:321px;width:300px;height:279px"></div>
  </div>
  <span class="size-label" style="left:527px;top:686px">300x600</span>

  <!-- 336x280 -->
  <div class="banner" style="left:631px;top:81px;width:336px;height:280px">
    <div class="brand" style="left:232px;top:12px;width:88px;height:31px;font-size:8px"><span class="brand__mark"></span>Pellmar Law Group</div>
    <h2 class="headline" style="top:56px;right:13px;font-size:27px">Injured in an accident?</h2>
    <p class="sub" style="top:86px;right:13px;font-size:12px">Contact us today for a free case evaluation</p>
    <div class="photo" role="img" aria-label="Photo of an attorney in conversation with a client in an office" style="left:0;top:114px;width:336px;height:166px"></div>
    <div class="cta" style="left:243px;top:249px;width:82px;height:21px;font-size:11px">Learn More<svg width="13" height="13" viewBox="0 0 14 14"><circle cx="7" cy="7" r="7" fill="#1f3a5c"/><path d="M5.5 4v6l4.5-3z" fill="#fff"/></svg></div>
  </div>
  <span class="size-label" style="left:906px;top:368px">336X280</span>

  <!-- 300x250 -->
  <div class="banner" style="left:631px;top:399px;width:300px;height:250px">
    <div class="brand" style="left:212px;top:12px;width:78px;height:27px;font-size:7px"><span class="brand__mark"></span>Pellmar Law Group</div>
    <h2 class="headline" style="top:51px;right:8px;font-size:24px">Injured in an accident?</h2>
    <p class="sub" style="top:78px;right:8px;font-size:11px">Contact us today for a free case evaluation</p>
    <div class="photo" role="img" aria-label="Photo of an attorney in conversation with a client in an office" style="left:0;top:101px;width:300px;height:149px"></div>
    <div class="cta" style="left:214px;top:207px;width:78px;height:21px;font-size:11px">Learn More<svg width="13" height="13" viewBox="0 0 14 14"><circle cx="7" cy="7" r="7" fill="#1f3a5c"/><path d="M5.5 4v6l4.5-3z" fill="#fff"/></svg></div>
  </div>
  <span class="size-label" style="left:871px;top:656px">300X250</span>

  <!-- 600x160 -->
  <div class="banner" style="left:79px;top:720px;width:600px;height:160px">
    <div class="photo photo--fade" role="img" aria-label="Photo of an attorney in conversation with a client in an office" style="left:0;top:0;width:600px;height:160px"></div>
    <div class="brand" style="left:230px;top:15px;width:101px;height:34px;font-size:9px"><span class="brand__mark"></span>Pellmar Law Group</div>
    <h2 class="headline" style="top:22px;right:13px;font-size:33px;line-height:32px">Alaska Personal<br>Injury Attorneys</h2>
    <p class="sub" style="top:96px;right:13px;font-size:12px">Learn more before you talk to the adjuster</p>
    <div class="cta" style="left:441px;top:126px;width:144px;height:22px;font-size:12px">For a free consultation<svg width="14" height="14" viewBox="0 0 14 14"><circle cx="7" cy="7" r="7" fill="#1f3a5c"/><path d="M5.5 4v6l4.5-3z" fill="#fff"/></svg></div>
  </div>
  <span class="size-label" style="left:620px;top:887px">600X160</span>

  <!-- 350x60 -->
  <div class="banner" style="left:79px;top:912px;width:350px;height:60px">
    <div class="photo" role="img" aria-label="Photo of an attorney in conversation with a client in an office" style="left:0;top:0;width:210px;height:60px"></div>
    <div class="brand" style="left:149px;top:5px;width:62px;height:21px;font-size:5.5px;gap:2px;padding:0 3px"><span class="brand__mark"></span>Pellmar Law Group</div>
    <h2 class="headline" style="top:6px;right:7px;font-size:17px">Accidents hurt</h2>
    <p class="sub" style="top:25px;right:7px;font-size:10px">We're here to help</p>
    <div class="cta" style="left:243px;top:42px;width:100px;height:14px;font-size:8px;padding:0 2px 0 4px">For a free consultation<svg width="10" height="10" viewBox="0 0 14 14"><circle cx="7" cy="7" r="7" fill="#1f3a5c"/><path d="M5.5 4v6l4.5-3z" fill="#fff"/></svg></div>
  </div>
  <span class="size-label" style="left:377px;top:979px">350X60</span>

</div>
</body>
</html>
```